Need website redesign!

I have a site, www.pinebrookfitcamp.com

I am looking to have it redesigned to make it simpler, and encourage people who hit the home page to click on a service, opt in, or contact me for more info. Having a video front and center with icons representing the services we offer around it may be a good idea, but I am open to YOUR design. Conversion is my goal. I want it to be friendly, but convey the fun and ENERGY of my bootcamp. Scrolling pics on home page so people can get a feel for our bootcamp is recommended as well.

```html
<!DOCTYPE html>
<html lang="en">
<head>
<meta charset="utf-8">
<title>Pinebrook Fit Camp</title>
<link rel="stylesheet" href="https://fonts.googleapis.com/css2?family=Raleway:wght@400;500;600;700;800&display=swap">
<style>
:root{
  --red:#ee1c25;
  --black:#000000;
  --navy:#14122b;
  --footer:#1b1b1b;
  --grey:#f0efec;
  --card:#eeece8;
  --text:#222222;
  --muted:#555555;
  --white:#ffffff;
  --blue:#3b5998;
}
*{box-sizing:border-box;margin:0;padding:0}
html,body{width:1200px;height:2299px;overflow:hidden}
body{position:relative;font-family:'Raleway',sans-serif;color:var(--text);background:var(--white)}
.abs{position:absolute}

.site-header{left:0;top:0;width:1200px;height:100px;background:var(--black);border-bottom:2px solid var(--red)}
.brand{position:absolute;left:92px;top:0;width:112px;height:110px;background:var(--black);display:flex;flex-direction:column;align-items:center;justify-content:center;gap:6px;z-index:2}
.brand-name{color:var(--red);font-weight:800;font-size:17px;line-height:1.05;text-align:center}
.brand-url{color:var(--white);font-weight:600;font-size:6px;letter-spacing:.3px}
.main-nav{position:absolute;right:90px;top:43px;display:flex;gap:22px}
.main-nav a{color:var(--red);font-weight:700;font-size:12.5px;text-decoration:none;text-transform:uppercase}
.main-nav a.active{color:var(--white)}

.hero{left:0;top:102px;width:1200px;height:608px;background:linear-gradient(120deg,#e9dcc8 0%,#c9b79b 40%,#8aa36d 60%,#d8c6ad 85%,#6c5a4a 100%)}
.hero-title{position:absolute;left:90px;top:40px;color:var(--red);font-weight:800;font-size:43px;line-height:49px}

.service-band{left:0;top:710px;width:1200px;height:102px;background:var(--navy);color:var(--white);display:flex;align-items:center;justify-content:center;font-size:27px;font-weight:600}

.video{left:91px;top:860px;width:338px;height:265px;background:var(--black)}
.video-title{position:absolute;left:12px;top:10px;color:var(--white);font-size:12px}
.video-frame{position:absolute;left:95px;top:30px;width:150px;height:200px;background:linear-gradient(180deg,#c69a6a,#6a4b34)}
.video-bar{position:absolute;left:0;bottom:0;width:338px;height:36px;background:#1c1c1c}
.video-progress{position:absolute;left:0;top:-4px;width:338px;height:4px;background:#555}
.video-progress span{display:block;width:22px;height:4px;background:var(--red)}
.video-time{position:absolute;left:98px;top:11px;color:var(--white);font-size:10px}

.intro{left:480px;top:895px;width:460px}
.intro h1{font-weight:500;font-size:27px;margin-bottom:16px}
.intro p{font-size:11.5px;line-height:21px;color:var(--text)}
.intro-actions{display:flex;gap:8px;margin-top:18px}
.btn{display:inline-flex;align-items:center;justify-content:center;height:26px;padding:0 14px;font-size:11px;color:var(--white);text-decoration:none}
.btn-red{background:var(--red)}
.btn-dark{background:var(--navy);font-weight:700;text-transform:uppercase}
.btn-blue{background:var(--blue);font-weight:700;text-transform:uppercase}

.section-rule{left:90px;top:1195px;width:1030px;height:1px;background:#cccccc}
.section-head{left:458px;top:1173px;width:292px;height:44px;background:var(--white);display:flex;align-items:center;justify-content:space-between;padding:0 18px}
.section-head h2{font-weight:500;font-size:27px}
.arrow-btn{width:36px;height:36px;border-radius:50%;background:#ececec;display:flex;align-items:center;justify-content:center}

.services{left:90px;top:1270px;display:flex;gap:9px}
.service-card{width:251px;height:198px;background:var(--card);text-align:center}
.service-photo{height:130px}
.service-card h3{font-weight:500;font-size:22px;margin:10px 0 8px}
.service-card .btn{height:24px;font-size:11px}

.optin{left:90px;top:1529px;width:1030px;height:174px;background:var(--grey);border-bottom:2px solid var(--red)}
.optin-text{position:absolute;left:50px;top:32px;color:var(--red);font-weight:800;font-size:26px;line-height:32px}
.field{position:absolute;top:56px}
.field label{display:block;font-size:12px;font-weight:500;margin-bottom:5px}
.field .input{width:203px;height:32px;border:1.5px solid var(--red);background:var(--white);font-size:11px;color:#999;padding:9px 12px}
.optin .btn-dark{position:absolute;left:843px;top:69px;height:32px;width:146px;font-size:11px}

.tagline{left:0;top:1748px;width:1200px;text-align:center;font-size:23px;line-height:31px;color:var(--text)}
.tagline strong{color:var(--red);font-weight:800}

.gallery{left:90px;top:1887px;display:flex;gap:9px}
.thumb{width:143px;height:106px}
.gallery-cta{left:851px;top:1887px;width:269px;height:106px;background:var(--red);color:var(--white);font-weight:700;font-size:23px;line-height:28px;padding:14px 24px}
.gallery-cta svg{position:absolute;right:18px;top:26px}

.site-footer{left:0;top:2082px;width:1200px;height:178px;background:var(--footer)}
.footer-brand{left:90px;top:2061px;width:114px;height:111px;background:var(--black);display:flex;flex-direction:column;align-items:center;justify-content:center;gap:6px}
.footer-address{left:92px;top:2177px;color:var(--white);font-size:10.5px;line-height:13px}
.footer-address p+p{margin-top:8px}
.footer-nav{left:604px;top:2111px;list-style:none}
.footer-nav li{color:var(--white);font-size:11px;height:21.5px;padding-left:28px;position:relative}
.footer-nav li.current::before{content:"";position:absolute;left:0;top:6px;width:18px;height:3px;background:var(--red)}
.locations{left:804px;top:2106px;color:var(--white);font-size:11px;display:flex;align-items:center;gap:6px}
.map{left:804px;top:2125px;width:316px;height:123px;background:linear-gradient(135deg,#eef0ea,#dfe3dc)}

.bottom-bar{left:0;top:2260px;width:1200px;height:39px;background:var(--black);color:var(--white);font-size:11px}
.copyright{position:absolute;left:92px;top:13px}
.legal{position:absolute;left:802px;top:13px;display:flex;gap:10px}
.social{position:absolute;left:1040px;top:9px;display:flex;gap:6px}
.social span{width:21px;height:21px;border-radius:50%}
</style>
</head>
<body>

<header class="site-header abs">
  <div class="brand"><span class="brand-name">PINEBROOK<br>FIT CAMP</span><span class="brand-url">WWW.PINEBROOKFITCAMP.COM</span></div>
  <nav class="main-nav">
    <a class="active">Home</a><a>Services</a><a>Classes</a><a>About Us</a><a>FAQ's</a><a>Contact Us</a>
  </nav>
</header>

<section class="hero abs" role="img" aria-label="Smiling woman in a teal top doing a side leg raise on a purple mat in a bright studio">
  <h2 class="hero-title">Morning,<br>Evening and<br>Weekend Hours!</h2>
</section>

<div class="service-band abs">Fat Loss Bootcamps, Martial Arts, Yoga, Kids Fitness, Personal Training</div>

<div class="video abs">
  <div class="video-title">Dan R lost 15 pounds in just 17 sessi...</div>
  <div class="video-frame" role="img" aria-label="Testimonial video still of a member speaking to camera"></div>
  <div class="video-bar">
    <div class="video-progress"><span></span></div>
    <svg class="abs" style="left:12px;top:11px" width="14" height="14" viewBox="0 0 14 14"><path d="M2 1 L12 7 L2 13Z" fill="#ddd"/></svg>
    <svg class="abs" style="left:40px;top:11px" width="18" height="14" viewBox="0 0 18 14"><path d="M1 5h4l5-4v12l-5-4H1z" fill="#ddd"/></svg>
    <span class="video-time">0:00 / 0:16</span>
    <svg class="abs" style="left:312px;top:11px" width="14" height="14" viewBox="0 0 14 14"><path d="M1 5V1h4M9 1h4v4M13 9v4H9M5 13H1V9" stroke="#ddd" stroke-width="1.5" fill="none"/></svg>
  </div>
</div>

<div class="intro abs">
  <h1>What is Pinebrook Fit Camp</h1>
  <p>Lorem Ipsum is simply dummy text of the printing and typesetting industry. Lorem Ipsum has been the industry's standard dummy text ever since the 1500s, when ... unknown printer took a galley of type and scrambled it to make a type specimen book.Lorem Ipsum is simply standard dummy text ever since the 1500s, when ... unknown printer took a galley of type and scrambled it to make a type specimen book.</p>
  <div class="intro-actions">
    <a class="btn btn-red">Read More</a>
    <a class="btn btn-dark">Get Started Now</a>
    <a class="btn btn-blue">Follow Us On Clubfeed</a>
  </div>
</div>

<div class="section-rule abs"></div>
<div class="section-head abs">
  <span class="arrow-btn"><svg width="12" height="14" viewBox="0 0 12 14"><path d="M8 1 L3 7 L8 13" stroke="#aaa" stroke-width="1.6" fill="none"/></svg></span>
  <h2>Our Services</h2>
  <span class="arrow-btn"><svg width="12" height="14" viewBox="0 0 12 14"><path d="M4 1 L9 7 L4 13" stroke="#222" stroke-width="1.6" fill="none"/></svg></span>
</div>

<div class="services abs">
  <article class="service-card"><div class="service-photo" role="img" aria-label="Group doing battle rope training in a gym" style="background:linear-gradient(180deg,#5a5a5a,#c23a3a)"></div><h3>Boot Camp</h3><a class="btn btn-red">Read More</a></article>
  <article class="service-card"><div class="service-photo" role="img" aria-label="Trainer coaching a client on suspension straps" style="background:linear-gradient(180deg,#d9d3cc,#4a5f8a)"></div><h3>Personal Training</h3><a class="btn btn-red">Read More</a></article>
  <article class="service-card"><div class="service-photo" role="img" aria-label="Woman stretching on a pink yoga mat" style="background:linear-gradient(180deg,#f1ebe3,#d9b9a0)"></div><h3>Yoga</h3><a class="btn btn-red">Read More</a></article>
  <article class="service-card"><div class="service-photo" role="img" aria-label="Child wearing red boxing gloves" style="background:linear-gradient(135deg,#3a3a3a,#b82a2a)"></div><h3>Kids Sports/ Agility</h3><a class="btn btn-red">Read More</a></article>
</div>

<section class="optin abs">
  <p class="optin-text">Leave your email for a<br>FREE week of bootcamp,<br>NO OBLIGATION</p>
  <div class="field" style="left:414px"><label>Name</label><div class="input">Enter Your Name</div></div>
  <div class="field" style="left:630px"><label>Email</label><div class="input">Enter Your Email ID</div></div>
  <a class="btn btn-dark">Get Started Now</a>
</section>

<p class="tagline abs">A fun, friendly, and effective place for you to shed serious fat,<br>build tight lean muscle, and have the time of your life doing it.<br>So...what are you waiting for? Register now and try us out <strong>RISK FREE!</strong></p>

<div class="gallery abs">
  <div class="thumb" role="img" aria-label="Member doing crunches on a mat" style="background:linear-gradient(135deg,#9ab07a,#4a4a4a)"></div>
  <div class="thumb" role="img" aria-label="Group posing outdoors in the woods" style="background:linear-gradient(135deg,#8fa86a,#5b6e8a)"></div>
  <div class="thumb" role="img" aria-label="Trainer with client on suspension straps" style="background:linear-gradient(135deg,#d6d0c8,#3c4f7a)"></div>
  <div class="thumb" role="img" aria-label="Members exercising on an outdoor field" style="background:linear-gradient(135deg,#6e9a4a,#3f7a2e)"></div>
  <div class="thumb" role="img" aria-label="Members training in a teal studio" style="background:linear-gradient(135deg,#4fa9a0,#c9c2b5)"></div>
</div>
<div class="gallery-cta abs">See Our<br>Complete<br>Photo Gallery
  <svg width="22" height="54" viewBox="0 0 22 54"><path d="M2 2 L20 27 L2 52" stroke="#fff" stroke-width="1.8" fill="none"/></svg>
</div>

<footer class="site-footer abs"></footer>
<div class="footer-brand abs"><span class="brand-name">PINEBROOK<br>FIT CAMP</span><span class="brand-url">WWW.PINEBROOKFITCAMP.COM</span></div>
<div class="footer-address abs">
  <p>Ridgeview Tae Kwon Do-Maple Commons<br>1820 Harlow Lane, Eastbrook, MD 21990</p>
  <p>Westfield Pinebrook Fit Camp<br>4410 Market Court, Suite B, Westfield, MD 21995</p>
</div>
<ul class="footer-nav abs">
  <li class="current">Home</li><li>Services</li><li>Classes</li><li>About Us</li><li>Join Now</li><li>Contact Us</li>
</ul>
<div class="locations abs">Our Locations <svg width="10" height="6" viewBox="0 0 10 6"><path d="M1 1 L5 5 L9 1" stroke="#fff" stroke-width="1.2" fill="none"/></svg></div>
<div class="map abs" role="img" aria-label="Street map showing the studio location with a red pin"></div>

<div class="bottom-bar abs">
  <span class="copyright">© 2014 Pinebrook Fit Camp</span>
  <span class="legal"><span>Privacy Policy</span><span>|</span><span>Disclaimer</span></span>
  <span class="social"><span style="background:#3b5998"></span><span style="background:#1da1f2"></span><span style="background:#dd4b39"></span></span>
</div>

</body>
</html>
```